olvar stationery

we have a logo and it is in the upload files. Please use the logos in denatured color effect from the same color pantone.
We would like to see a stationery design for a new company working worldwide in the petrochemical sector as an agent.
Please use our logo to create business card, presentation folder, letterhead, envelope,note pad, note books etc etc.
Of course we want convey security and stability, in terms of finance and connections

Target Market(s)

Multinational enterprise, executive, professional,

Industry/Entity Type

Business

Font styles to use
Serif

Colors
0756a3
3176b5
85acd3
86cae6
87c9e5
33a6d7
0692cd

Requirements
Must have
• business cards must have option for address name, title, email telephone etc. I like business card that is both side.

Color as I stated DESAUTERED color effect based on the original color,

I LIKE MATTE effect
Nice to have
• all the pieces must be cohesive. I like print raised for business cards
Should not have
• Shiny finish

```html
<!DOCTYPE html>
<html lang="en">
<head>
<meta charset="utf-8">
<title>Olvar Group – Letterhead and Fax Sheet</title>
<link rel="stylesheet" href="https://fonts.googleapis.com/css2?family=Arimo:wght@400;700&display=swap">
<style>
  :root{
    --backdrop:#ebebeb;
    --paper:#f4f4f4;
    --navy:#34508a;
    --band-grey:#c9cbcf;
    --ink-grey:#5a5a5a;
    --rule-grey:#8c8c8c;
    --cell-fill:#e2e3e5;
    --footer-ink:#6b6f76;
  }
  *{box-sizing:border-box;margin:0;padding:0}
  html,body{width:1200px;height:815px;overflow:hidden;background:var(--backdrop)}
  .canvas{position:relative;width:1200px;height:815px}
  .sheet{position:absolute;top:72px;width:482px;height:681px;background:var(--paper);overflow:hidden}
  .sheet--letterhead{left:80px}
  .sheet--fax{left:638px}

  .brand{position:absolute;left:44px;top:50px;font-family:"Arimo",sans-serif;font-weight:700;font-size:22px;letter-spacing:.5px;color:var(--navy)}

  .footer{position:absolute;left:38px;top:634px;display:flex;align-items:stretch;font-family:"Arimo",sans-serif;font-size:7px;line-height:10px;color:var(--footer-ink)}
  .footer__group{padding-right:12px;margin-right:10px;border-right:1px solid var(--band-grey)}
  .footer__group:last-child{border:none;margin:0;padding:0}
  .footer__line{display:flex;align-items:center;gap:5px}
  .footer__icon{width:7px;height:7px}

  .band-grey{position:absolute;left:0;right:0;top:669px;height:4px;background:var(--band-grey)}
  .band-navy{position:absolute;left:0;right:0;top:673px;height:8px;background:var(--navy)}

  .fax-title{position:absolute;left:327px;top:32px;font-family:"Arimo",sans-serif;font-weight:400;font-size:62px;line-height:1;color:var(--ink-grey);letter-spacing:1px}

  .fax-details{position:absolute;left:37px;top:139px;width:413px;border-collapse:collapse;font-family:"Arimo",sans-serif;font-size:7.5px;font-weight:700;color:var(--ink-grey)}
  .fax-details td{border:1px solid var(--rule-grey);height:14.5px;padding:0 4px}
  .fax-details .label{width:43px}
  .fax-details .value{width:162px}
  .fax-details .label--right{width:45px}

  .fax-options{position:absolute;left:37px;top:227px;width:413px;display:flex;border:1px solid var(--rule-grey);background:var(--cell-fill);height:16px;font-family:"Arimo",sans-serif;font-size:7.5px;font-weight:700;color:var(--ink-grey)}
  .fax-options__item{flex:1;display:flex;align-items:center;justify-content:center;gap:4px;border-right:1px solid var(--rule-grey)}
  .fax-options__item:last-child{border:none}
  .fax-options__box{width:5px;height:5px;border:1px solid var(--rule-grey)}

  .fax-comments{position:absolute;left:37px;top:242px;width:413px;height:372px;border:1px solid var(--rule-grey);border-top:none;font-family:"Arimo",sans-serif;font-size:7.5px;color:var(--ink-grey);text-align:center;padding-top:12px}
</style>
</head>
<body>
<div class="canvas">

  <section class="sheet sheet--letterhead">
    <div class="brand">Olvar Group</div>
    <div class="footer">
      <div class="footer__group"><div>Lenta 12c, Brod</div><div>10 020 KALMAR</div></div>
      <div class="footer__group">
        <div class="footer__line"><svg class="footer__icon" viewBox="0 0 10 10"><circle cx="5" cy="5" r="4.5" fill="none" stroke="#34508a"/><path d="M3.3 2.8l1 1-.6.7c.4.8 1 1.4 1.8 1.8l.7-.6 1 1-.8.8C4.8 7.3 2.7 5.2 2.5 3.6z" fill="#34508a"/></svg>+385 1 44 20 318</div>
        <div class="footer__line"><svg class="footer__icon" viewBox="0 0 10 10"><circle cx="5" cy="5" r="4.5" fill="#34508a"/><rect x="2.5" y="3.5" width="5" height="3" fill="#f4f4f4"/></svg>+385 1 44 20 319</div>
      </div>
      <div class="footer__group">
        <div class="footer__line"><svg class="footer__icon" viewBox="0 0 10 10"><circle cx="5" cy="5" r="4.5" fill="#34508a"/><path d="M2.5 3.5h5v3h-5zM2.5 3.5l2.5 2 2.5-2" fill="none" stroke="#f4f4f4" stroke-width=".8"/></svg>info@olvargroup.com</div>
        <div class="footer__line"><svg class="footer__icon" viewBox="0 0 10 10"><circle cx="5" cy="5" r="4.5" fill="#34508a"/><path d="M1 5h8M5 1v8" stroke="#f4f4f4" stroke-width=".7"/></svg>www.olvargroup.com</div>
      </div>
    </div>
    <div class="band-grey"></div><div class="band-navy"></div>
  </section>

  <section class="sheet sheet--fax">
    <div class="brand">Olvar Group</div>
    <h1 class="fax-title">FAX</h1>

    <table class="fax-details">
      <tr><td class="label">To:</td><td class="value"></td><td class="label label--right">From:</td><td></td></tr>
      <tr><td class="label">Fax:</td><td class="value"></td><td class="label label--right">Pages:</td><td></td></tr>
      <tr><td class="label">Phone:</td><td class="value"></td><td class="label label--right">Date:</td><td></td></tr>
      <tr><td class="label">Re:</td><td class="value"></td><td class="label label--right">CC:</td><td></td></tr>
    </table>

    <div class="fax-options">
      <div class="fax-options__item"><span class="fax-options__box"></span>Urgent</div>
      <div class="fax-options__item"><span class="fax-options__box"></span>For Review</div>
      <div class="fax-options__item"><span class="fax-options__box"></span>Please Comment</div>
      <div class="fax-options__item"><span class="fax-options__box"></span>Please Reply</div>
      <div class="fax-options__item"><span class="fax-options__box"></span>Please Recycle</div>
    </div>
    <div class="fax-comments">COMMENTS:</div>

    <div class="footer">
      <div class="footer__group"><div>Lenta 12c, Brod</div><div>10 020 KALMAR</div></div>
      <div class="footer__group">
        <div class="footer__line"><svg class="footer__icon" viewBox="0 0 10 10"><circle cx="5" cy="5" r="4.5" fill="none" stroke="#34508a"/><path d="M3.3 2.8l1 1-.6.7c.4.8 1 1.4 1.8 1.8l.7-.6 1 1-.8.8C4.8 7.3 2.7 5.2 2.5 3.6z" fill="#34508a"/></svg>+385 1 44 20 318</div>
        <div class="footer__line"><svg class="footer__icon" viewBox="0 0 10 10"><circle cx="5" cy="5" r="4.5" fill="#34508a"/><rect x="2.5" y="3.5" width="5" height="3" fill="#f4f4f4"/></svg>+385 1 44 20 319</div>
      </div>
      <div class="footer__group">
        <div class="footer__line"><svg class="footer__icon" viewBox="0 0 10 10"><circle cx="5" cy="5" r="4.5" fill="#34508a"/><path d="M2.5 3.5h5v3h-5zM2.5 3.5l2.5 2 2.5-2" fill="none" stroke="#f4f4f4" stroke-width=".8"/></svg>info@olvargroup.com</div>
        <div class="footer__line"><svg class="footer__icon" viewBox="0 0 10 10"><circle cx="5" cy="5" r="4.5" fill="#34508a"/><path d="M1 5h8M5 1v8" stroke="#f4f4f4" stroke-width=".7"/></svg>www.olvargroup.com</div>
      </div>
    </div>
    <div class="band-grey"></div><div class="band-navy"></div>
  </section>

</div>
</body>
</html>
```